Business Card Design

Marla Quenby
Artist of Contemporary/Modern/Representational Art
Contact: 0429175348
Please include my web site (thanks)! http://www.artloft583.com.au/marla-quenby
And
Email: marlaquenby@vexmail.com

Target Market(s)

Modern professional People who know what they like in modern contemporary art and have the means to purchase it.

Industry/Entity Type

Business

Contact Information for Business Card

Marla Quenby
Contact: 0429175348

Font styles to use
Sans Serif

Requirements
Must have
• Simplicity & to the point
Keep the font modern/ contemporary
Nice to have
• A portrait of me and one piece of work on the business card (one on each side).
Should not have
• I'm not into butterflies.
No feminine style swirls
Nor I like swirls that look like tatoos

```html
<!DOCTYPE html>
<html lang="en">
<head>
<meta charset="utf-8">
<title>Marla Quenby – Business Card</title>
<link href="https://fonts.googleapis.com/css2?family=Quicksand:wght@500;700&family=Open+Sans:wght@400;600&display=swap" rel="stylesheet">
<style>
  :root {
    --page: #e9e9ec;
    --card-blue: #4d9ed6;
    --card-blue-dark: #3a86bf;
    --band-grey: #3b3d42;
    --card-dark: #2b2b2e;
    --frame: #1f1f22;
    --accent: #2f9ee3;
    --white: #ffffff;
    --rule: rgba(255,255,255,0.85);
  }
  * { box-sizing: border-box; margin: 0; padding: 0; }
  html, body { width: 1200px; height: 849px; overflow: hidden; background: var(--page); }
  .canvas { position: relative; width: 1200px; height: 849px; }

  .card {
    position: absolute; width: 560px; height: 320px;
    border-radius: 18px; overflow: hidden;
    box-shadow: 0 10px 30px rgba(0,0,0,0.25);
  }

  /* Back side */
  .card--back { left: 60px; top: 70px; background: var(--card-blue); }
  .back-band { position: absolute; inset: 0; width: 100%; height: 100%; }
  .artwork-frame {
    position: absolute; left: 58px; top: 112px; width: 220px; height: 150px;
    background: var(--frame); padding: 12px;
  }
  .artwork {
    display: block; width: 100%; height: 100%;
    background: linear-gradient(135deg, #6aa3c8 0%, #c8573a 40%, #e0a54a 60%, #4d7e8e 100%);
  }
  .back-divider {
    position: absolute; left: 300px; top: 120px; width: 1px; height: 132px;
    background: var(--rule);
  }
  .contact-list {
    position: absolute; left: 318px; top: 118px; width: 230px; list-style: none;
    font-family: "Open Sans", sans-serif; color: var(--white); font-size: 12.5px; line-height: 1.3;
  }
  .contact-list li { display: flex; align-items: flex-start; gap: 9px; margin-bottom: 12px; }
  .contact-icon { flex: 0 0 14px; width: 14px; height: 14px; margin-top: 1px; }

  /* Front side */
  .card--front { left: 580px; top: 450px; background: var(--card-dark); }
  .front-art { position: absolute; left: 0; top: 0; width: 100%; height: 100%; }
  .portrait {
    position: absolute; left: 128px; top: 190px; width: 72px; height: 78px;
    border: 4px solid var(--accent); background: linear-gradient(160deg, #8a6a5a, #c24a3a 70%, #3a2a2a);
  }
  .identity { position: absolute; left: 212px; top: 214px; width: 330px; font-family: "Quicksand", sans-serif; }
  .identity__name { color: var(--accent); font-weight: 700; font-size: 30px; line-height: 1.1; letter-spacing: 0.5px; padding-left: 52px; white-space: nowrap; }
  .identity__role { color: var(--accent); font-weight: 500; font-size: 11px; margin-top: 4px; white-space: nowrap; }
</style>
</head>
<body>
<main class="canvas">

  <section class="card card--back" aria-label="Card back">
    <svg class="back-band" viewBox="0 0 560 320" preserveAspectRatio="none" aria-hidden="true">
      <path d="M0 0 H560 V40 C420 30 330 95 210 100 C120 104 50 70 0 58 Z" fill="var(--band-grey)"/>
      <path d="M0 58 C50 70 120 104 210 100 C330 95 420 30 560 40 V52 C420 44 330 108 210 112 C120 116 50 84 0 72 Z" fill="var(--card-blue-dark)"/>
    </svg>
    <div class="artwork-frame">
      <div class="artwork" role="img" aria-label="Painting of a colourful harbour town with red roofs and a church spire"></div>
    </div>
    <div class="back-divider"></div>
    <ul class="contact-list">
      <li>
        <svg class="contact-icon" viewBox="0 0 14 14" aria-hidden="true"><circle cx="7" cy="7" r="6" fill="none" stroke="#fff" stroke-width="1.2"/><rect x="3.8" y="4.8" width="6.4" height="4.4" fill="none" stroke="#fff" stroke-width="1"/><path d="M3.8 4.8 L7 7.4 L10.2 4.8" fill="none" stroke="#fff" stroke-width="1"/></svg>
        <span>marlaquenby@vexmail.com</span>
      </li>
      <li>
        <svg class="contact-icon" viewBox="0 0 14 14" aria-hidden="true"><circle cx="7" cy="7" r="6" fill="none" stroke="#fff" stroke-width="1.2"/><circle cx="7" cy="7" r="3.2" fill="none" stroke="#fff" stroke-width="1"/><path d="M3.8 7 H10.2" stroke="#fff" stroke-width="1"/></svg>
        <span>http://www.artloft583.com.au/<br>marla-quenby</span>
      </li>
      <li>
        <svg class="contact-icon" viewBox="0 0 14 14" aria-hidden="true"><circle cx="7" cy="7" r="6" fill="none" stroke="#fff" stroke-width="1.2"/><path d="M4.8 4 L6 4 L6.6 5.8 L5.8 6.5 C6.2 7.4 6.8 8 7.6 8.3 L8.3 7.5 L10 8.1 L10 9.3 C7.3 9.9 4.2 6.8 4.8 4 Z" fill="#fff"/></svg>
        <span>0429175348</span>
      </li>
    </ul>
  </section>

  <section class="card card--front" aria-label="Card front">
    <svg class="front-art" viewBox="0 0 560 320" preserveAspectRatio="none">
      <defs>
        <linearGradient id="aerial" x1="0" y1="0" x2="1" y2="1">
          <stop offset="0" stop-color="#5a8fb0"/>
          <stop offset="0.5" stop-color="#5f8a4a"/>
          <stop offset="1" stop-color="#8a8f8c"/>
        </linearGradient>
        <linearGradient id="houses" x1="0" y1="0" x2="1" y2="0">
          <stop offset="0" stop-color="#c23a32"/>
          <stop offset="0.35" stop-color="#8fb36a"/>
          <stop offset="0.6" stop-color="#e0b83a"/>
          <stop offset="1" stop-color="#7aa65a"/>
        </linearGradient>
        <linearGradient id="stripe" x1="0" y1="0" x2="1" y2="0">
          <stop offset="0" stop-color="#3a6f9a"/>
          <stop offset="0.5" stop-color="#b8443a"/>
          <stop offset="1" stop-color="#d0a040"/>
        </linearGradient>
      </defs>
      <polygon points="0,0 310,0 280,118 0,72" fill="url(#aerial)" role="img" aria-label="Painting of an aerial city view with a winding river and stadium"/>
      <polygon points="310,0 560,0 560,160 280,118" fill="url(#houses)" role="img" aria-label="Painting of a row of colourful gabled townhouses under a blue sky"/>
      <polygon points="0,72 560,160 560,170 0,82" fill="#1c1c1e"/>
      <polygon points="0,86 560,174 560,182 0,94" fill="url(#stripe)" role="img" aria-label="Thin band of painted colour"/>
    </svg>
    <div class="portrait" role="img" aria-label="Portrait photo of the artist"></div>
    <div class="identity">
      <h1 class="identity__name">Marla Quenby</h1>
      <p class="identity__role">Artist of Contemporary/Modern/Representational Art</p>
    </div>
  </section>

</main>
</body>
</html>
```